3 Politically Incorrect Greeting Cards

I would like to see some clean, colorful, and modern designs for 3 "politically incorrect" greeting cards aimed at young, single, successful women. I would like them to say:

Card 1: " Congratulations on not marrying the wrong person"
Card 2: " Congratulations on buying a house without a husband"
Card 3: " Thank you for not forgetting about me now that you have a boyfriend"

My initial thought was to have a white background with simple black writing, but I think a colorful background with a white text box in the middle might be more appropriate. I can't imagine the cards having any images/icons on them, but I'm open to suggestions if you think it would improve on the design. You guys are likely more creative than I am.

I've included a couple pics of looks I like - but like I said - I'm open to suggestions and what I like may not be appropriate for these cards. All the cards can have a similar esthetic or theme (maybe the same fonts but different colors or different color florals in each) or they can be completely different.

Target Market(s)

Young, single, successful women mid-20s to mid 40's.

Font styles to use
Serif
Sans Serif
Other font styles liked:
• Watercolour lettering maybe

Colors

Designer to choose colors to be used in the design.

Requirements
Must have
• Clean, colorful, bright, professional looking. The right tone for the message.
• I think the message is bold so the writing and colors have to be as well. I have included examples of ideas I like.
Nice to have
• Images, illustrations, icons, maybe patterns or some decorative details. Something to make the card more interesting than just the words (like the blue background with black letters one I made). I like a bright pattern with a white box in the center with the text.
Should not have
• Special effects, galaxy pictures, ugly images, bland colors.

```html
<!DOCTYPE html>
<html lang="en">
<head>
<meta charset="utf-8">
<title>Congratulations on not marrying the wrong person — greeting card</title>
<link rel="stylesheet" href="https://fonts.googleapis.com/css2?family=Kaushan+Script&display=swap">
<style>
  :root {
    --page-bg: #f4f4f4;
    --card-bg: #ffffff;
    --wash-deep: #3cc0e2;
    --wash-mid: #8fdfea;
    --wash-mint: #a9f1ee;
    --wash-pale: #d6eef8;
    --lettering: #ffffff;
  }
  * { box-sizing: border-box; margin: 0; padding: 0; }
  html, body {
    width: 1200px;
    height: 1200px;
    overflow: hidden;
    background: var(--page-bg);
  }
  .card {
    position: absolute;
    left: 45px;
    top: 204px;
    width: 1114px;
    height: 784px;
    background: var(--card-bg);
    overflow: hidden;
  }
  .card__wash {
    position: absolute;
    inset: 0;
    width: 100%;
    height: 100%;
  }
  .card__message {
    position: absolute;
    left: 0;
    right: 0;
    top: 74px;
    text-align: center;
    font-family: "Kaushan Script", cursive;
    font-weight: 400;
    font-size: 98px;
    line-height: 126px;
    color: var(--lettering);
    letter-spacing: -1px;
  }
  .card__line { display: block; }
</style>
</head>
<body>
  <main class="card">
    <svg class="card__wash" viewBox="0 0 1114 784" role="img" aria-label="Soft blue and mint watercolour wash behind the message">
      <defs>
        <radialGradient id="wash-gradient" cx="0.45" cy="0.62" r="0.6">
          <stop offset="0" stop-color="var(--wash-deep)"/>
          <stop offset="0.45" stop-color="var(--wash-mid)"/>
          <stop offset="0.8" stop-color="var(--wash-mint)"/>
          <stop offset="1" stop-color="var(--wash-pale)"/>
        </radialGradient>
        <filter id="wash-soften" x="-10%" y="-10%" width="120%" height="120%">
          <feGaussianBlur stdDeviation="10"/>
        </filter>
      </defs>
      <path filter="url(#wash-soften)" fill="url(#wash-gradient)"
        d="M40 80 C140 40 240 40 340 20 C520 -10 760 0 960 40 C1040 70 1070 200 1070 330
           C1080 420 1060 520 1010 600 C950 700 860 770 760 790 L240 790
           C190 740 160 680 120 600 C60 520 40 420 60 330 C30 260 10 160 40 80 Z"/>
    </svg>
    <p class="card__message">
      <span class="card__line">Congratulations</span>
      <span class="card__line">on not</span>
      <span class="card__line">marrying</span>
      <span class="card__line">the wrong</span>
      <span class="card__line">person</span>
    </p>
  </main>
</body>
</html>
```